Business card for my new company (Accounting firm)

I need a business card for my new business Corvane Advisory and Ledger SA. Our services are accounting, tax, audit and financial management. Our customers are small companies, start-ups and new companies. The final design has to show financial security, trust and growth. Please find our logo attached to the business card. Text for the business card: Corvane Advisory and Ledger SA Tomas da Varela Director and Founder Certified Accountant Tel. 022 418 27 35 tv@corvaneconseil.ch www.corvaneconseil.ch Rue des Vergers-Bleus 14 1201 Geneva
Target Market(s)
Our customers are small companies, start-ups and new companies.
Industry/Entity Type
Finance And Accounting
Contact Information for Business Card
Corvane Conseil et Registre SA
Tomas da Varela
Directeur et Fondateur
Expert-comptable diplômé
Tél. 022 418 27 35
tv@corvaneconseil.ch
www.corvaneconseil.ch
Rue des Vergers-Bleus 14
1201 Genève

```html
<!DOCTYPE html>
<html lang="en">
<head>
<meta charset="utf-8">
<title>Corvane Business Cards</title>
<link rel="stylesheet" href="https://fonts.googleapis.com/css2?family=Open+Sans:wght@400;600;700;800&display=swap">
<style>
  :root {
    --page-bg: #2b2c2e;
    --card-white: #ffffff;
    --card-dark: #3a3b3e;
    --accent-blue: #2aa3d8;
    --accent-deep: #1b7fb8;
    --ink-dark: #3b3d40;
    --ink-light: #e6e8ea;
    --ink-muted: #c9ccd0;
  }
  * { margin: 0; padding: 0; box-sizing: border-box; }
  html, body {
    width: 1200px; height: 997px; overflow: hidden;
    background: var(--page-bg);
    font-family: "Open Sans", Arial, sans-serif;
  }
  .sheet {
    width: 1200px; height: 997px;
    display: flex; flex-direction: column;
    align-items: center; justify-content: center; gap: 24px;
  }
  .card {
    position: relative; width: 820px; height: 469px;
    background: var(--card-white); overflow: hidden;
    box-shadow: 0 10px 30px rgba(0,0,0,.45);
  }
  .card-art { position: absolute; inset: 0; }
  .brand {
    position: absolute; top: 66px; left: 0; width: 820px;
    display: flex; align-items: center; justify-content: center; gap: 16px;
  }
  .brand-mark { width: 38px; height: 38px; background: var(--accent-deep); }
  .brand-name {
    font-size: 50px; font-weight: 700; letter-spacing: 3px;
    color: var(--ink-dark); line-height: 1;
  }
  .person { position: absolute; left: 38px; top: 258px; }
  .person-name { color: var(--accent-blue); font-size: 18px; font-weight: 700; line-height: 26px; }
  .person-role { color: var(--ink-light); font-size: 13px; font-weight: 700; line-height: 18px; }
  .contact-list { list-style: none; margin-top: 8px; }
  .contact-item {
    display: flex; align-items: center; gap: 10px;
    color: var(--ink-light); font-size: 15px; line-height: 24px;
  }
  .contact-icon { width: 14px; height: 14px; fill: var(--accent-blue); flex: none; }
  .company {
    position: absolute; right: 40px; top: 330px; text-align right;
    text-align: right;
  }
  .company-name { color: var(--accent-blue); font-size: 15px; font-weight: 700; line-height: 22px; }
  .company-address { color: var(--ink-muted); font-size: 14px; line-height: 20px; }
  .services {
    position: absolute; left: 0; right: 0; bottom: 0; height: 44px;
    display: flex; align-items: center; justify-content: center;
    color: var(--card-white); font-size: 16px; font-weight: 800;
    letter-spacing: .4px; text-transform: uppercase;
  }
</style>
</head>
<body>
<main class="sheet">

  <article class="card card-front" lang="en">
    <svg class="card-art" viewBox="0 0 820 469" aria-hidden="true">
      <path d="M0,233 C260,203 560,278 820,138 L820,150 C560,290 260,215 0,245 Z" fill="var(--accent-blue)"/>
      <path d="M0,245 C260,215 560,290 820,150 L820,469 L0,469 Z" fill="var(--card-dark)"/>
      <path d="M330,212 C480,212 680,190 790,130" fill="none" stroke="var(--accent-blue)" stroke-width="4" stroke-linecap="round"/>
      <rect x="0" y="425" width="820" height="44" fill="var(--accent-blue)"/>
    </svg>
    <div class="brand"><span class="brand-mark"></span><span class="brand-name">CORVANE</span></div>
    <div class="company">
      <p class="company-name">Corvane Advisory &amp; Ledger SA</p>
      <p class="company-address">Rue des Vergers-Bleus 14,1201 Genève</p>
    </div>
    <div class="person">
      <p class="person-name">Tomas da Varela</p>
      <p class="person-role">Director/Founder Certified Accountant</p>
      <ul class="contact-list">
        <li class="contact-item"><svg class="contact-icon" viewBox="0 0 16 16"><path d="M2 5c0-2 2-3 6-3s6 1 6 3l-1 2-3-1V4H6v2L3 7zM4 8h8l2 6H2z"/></svg>022 418 27 35</li>
        <li class="contact-item"><svg class="contact-icon" viewBox="0 0 16 16"><path d="M1 3h14v10H1zM2 4l6 5 6-5v1L8 10 2 5z" fill-rule="evenodd"/></svg>tv@corvaneconseil.ch</li>
        <li class="contact-item"><svg class="contact-icon" viewBox="0 0 16 16"><path d="M8 1a7 7 0 1 0 0 14A7 7 0 0 0 8 1zm0 2a5 5 0 1 1 0 10A5 5 0 0 1 8 3z"/><path d="M3 7.3h10v1.4H3zM7.3 3h1.4v10H7.3z"/></svg>www.corvaneconseil.ch</li>
      </ul>
    </div>
    <p class="services">Our services are accounting, tax, audit &amp; financial management</p>
  </article>

  <article class="card card-back" lang="fr">
    <svg class="card-art" viewBox="0 0 820 469" aria-hidden="true">
      <path d="M0,233 C260,203 560,278 820,138 L820,150 C560,290 260,215 0,245 Z" fill="var(--accent-blue)"/>
      <path d="M0,245 C260,215 560,290 820,150 L820,469 L0,469 Z" fill="var(--card-dark)"/>
      <path d="M330,212 C480,212 680,190 790,130" fill="none" stroke="var(--accent-blue)" stroke-width="4" stroke-linecap="round"/>
      <rect x="0" y="425" width="820" height="44" fill="var(--accent-blue)"/>
    </svg>
    <div class="brand"><span class="brand-mark"></span><span class="brand-name">CORVANE</span></div>
    <div class="company">
      <p class="company-name">Corvane Advisory &amp; Ledger SA</p>
      <p class="company-address">Rue des Vergers-Bleus 14,1201 Genève</p>
    </div>
    <div class="person">
      <p class="person-name">Tomas da Varela</p>
      <p class="person-role">Directeur et Fondateur<br>Expert-comptable diplômé</p>
      <ul class="contact-list">
        <li class="contact-item"><svg class="contact-icon" viewBox="0 0 16 16"><path d="M2 5c0-2 2-3 6-3s6 1 6 3l-1 2-3-1V4H6v2L3 7zM4 8h8l2 6H2z"/></svg>022 418 27 35</li>
        <li class="contact-item"><svg class="contact-icon" viewBox="0 0 16 16"><path d="M1 3h14v10H1zM2 4l6 5 6-5v1L8 10 2 5z" fill-rule="evenodd"/></svg>tv@corvaneconseil.ch</li>
        <li class="contact-item"><svg class="contact-icon" viewBox="0 0 16 16"><path d="M8 1a7 7 0 1 0 0 14A7 7 0 0 0 8 1zm0 2a5 5 0 1 1 0 10A5 5 0 0 1 8 3z"/><path d="M3 7.3h10v1.4H3zM7.3 3h1.4v10H7.3z"/></svg>www.corvaneconseil.ch</li>
      </ul>
    </div>
    <p class="services">Our services are accounting, tax, audit &amp; financial management</p>
  </article>

</main>
</body>
</html>
```